Build our new website pages and templates

BACKGROUND
• We are migrating over from an old website and URL ( www.plotwharf.co.nz ) to a brand new website with a new URL – www.galbrook.co.nz
• We have already selected a logo for the new website – see attached.
• We manage all our websites in house using Dreamweaver and want to retain the capability of doing this for the new site.

-------------------------------------------------------------------------------------

BRIEF
• Design the new look galbrook website for our company including color palette, fonts, icons, graphics and layout.

• The design should reflect our high quality venue hire services to corporate buyers, picking up inspiration from our beautiful new logo

• The index page should also incorporate our:

o What We Do page
o How To Use Our Site page
o Are you a venue? content (with link to the 'List A Venue' page)
o Our key contact links
o Our navigation menu

Here are some examples of the types of Index pages that appeal to us:

http://wheretilesdrop.com/
What we like about it: Like the simplicity of the page and the scroll function to show different page elements.

http://www.qarvo.com/
What we like about it: Strong blocks of hero images and fonts. Easy scroll from one section to the next.

https://www.lumt.com/
What we like about it: Like the scroll feature to different sections.

https://www.pondtable.net/
What we like about it: Simple stylish Index page that scrolls easily

Our version would be:
1. Our logo centre page with hero image background
2. Scroll down to 'what we do' section with 3 bullet points and icons
3. Scroll down to 'how to use this site' section with 3 bullet points (1,2,3) and instructions
4. Are you a venue? instructions about how to talk to us about listing. And link to the 'how to list' page.

To the left we would want a burger menu with dropdown nav and links

• Design the template for the 'venue listings' pages
o We want to list venues by towns or cities and have one page dedicated for each. We would create each page from the template you provide.
o When the user clicks on any particular venue it clicks through to the individual venue page
o This page should have a map with pins for each listed venue

Here are some examples of the listings pages that we like and why:

http://www.qarvo.com/
What we like about it: Strong blocks and font. Nice hover feature changing the colour and introducing the click through arrow on the right bottom corner

http://www.gatherloft.co.nz/
What we like about it: Don’t like the colours or design but like the practicality of the search box and the 3 column listings when you select a search criteria. This is a familiar format and maybe easier for the user to understand and navigate around.

http://www.tidemarkhalls.co.nz/venues
What we like about it: Like the simplicity of this page but our listings would need a little more info beneath each one. The hover function is annoying!

• Design the template for the individual venue pages.
• Include a search function across the full site so that users can choose to search for venues in different towns or cities.
• Design the booking form pages for the individual venues (we have working examples of our existing ones)

• Design the payment page and thank you page for those who complete the booking form online. (We will be offering the option on our site to pay by credit card into our coinwell account) We have working examples of our current thank you and payment page although the payment page is not live on our current site.

------------------------------------------------------------------------------------

TECHNICAL
• Pages need to be created in html and css. Some php pages, as required for payment pages. And some javascript for all pages.

• Templates will need to be in dwt format, as we need to be able to upload to Dreamweaver CC and create new pages from the templates for new venues as and when necessary.

• Pages should be responsive for browsing across PC’s Laptops, ipads, phones and other devices.

• Website will be hosted on a Linux server when ready to go live.

A) We can provide existing website files if these help with the design and build process of the new site.
B) We plan to build additional features for the site, as a second phase project. This would include client login areas and electronic confirmations of bookings and online updating of booking forms.

Requirements
Must have
• See the brief provided. Successful designer/developer must be able to supply files in html, css, php (if required) and include javascript coding where necessary. We will be hosting these files and managing the site using Dreamweaver CC so full accessibility to the files is important.
Nice to have
• Notes have been added to the brief. Please read and ask questions if not clear.
Should not have
• We are not looking for a site to be built using an open source platform. The files provided must be able to be uploaded to our own server for our own management after the end of the project.

```html
<!DOCTYPE html>
<html lang="en">
<head>
<meta charset="utf-8">
<title>galbrook – Finding venues for you</title>
<link rel="stylesheet" href="https://fonts.googleapis.com/css2?family=Questrial&family=Open+Sans:wght@400;600;700&display=swap">
<style>
:root{
  --green:#8cb43c;
  --green-dark:#6f9a2a;
  --ink:#231f20;
  --ink-soft:#3a3637;
  --text:#2b2b2b;
  --muted:#8a8a8a;
  --light:#f2f2f2;
  --white:#ffffff;
}
*{box-sizing:border-box;margin:0;padding:0}
html,body{width:1200px;height:2655px;overflow:hidden}
body{font-family:"Open Sans",Arial,sans-serif;color:var(--text);background:var(--white);position:relative}
.abs{position:absolute}
h2.section-title{font-family:"Questrial",Arial,sans-serif;font-weight:400;font-size:42px;text-align:center;color:#444}

/* hero */
.hero{position:absolute;left:0;top:0;width:1200px;height:670px}
.hero-photo{position:absolute;inset:0;background:linear-gradient(180deg,#8fa9c0 0%,#5f7f98 25%,#6f7880 55%,#4a4f55 100%)}
.brand-box{position:absolute;left:494px;top:0;width:212px;height:150px;background:rgba(35,31,32,.92);display:flex;flex-direction:column;align-items:center;justify-content:center;gap:10px}
.brand-box .mark{width:52px;height:52px;border:3px solid var(--white);border-radius:50%}
.brand-name{font-family:"Open Sans",Arial,sans-serif;font-weight:600;color:var(--white);font-size:30px;letter-spacing:1px}
.main-nav{position:absolute;left:0;top:618px;width:1200px;height:52px;background:rgba(35,31,32,.93)}
.main-nav a{position:absolute;top:15px;color:var(--white);font-size:17px;font-style:italic;text-decoration:none}
.main-nav a.active{border-bottom:3px solid var(--green);padding-bottom:5px}
.burger{position:absolute;left:782px;top:14px;width:30px;height:24px}
.burger span{display:block;height:4px;background:var(--white);margin-bottom:6px}
.search-panel{position:absolute;left:862px;top:318px;width:216px;height:300px;background:var(--green);padding:0 10px}
.search-panel .head{background:var(--ink);margin:0 -10px;height:40px;color:var(--white);font-size:15px;font-weight:600;display:flex;align-items:center;gap:8px;padding-left:14px}
.search-panel label{display:block;color:var(--ink);font-size:11px;font-weight:700;margin:10px 0 4px}
.field{background:var(--white);height:20px;font-size:9px;color:var(--muted);padding:4px 8px;margin-bottom:6px;position:relative}
.field.select::after{content:"";position:absolute;right:7px;top:8px;border:4px solid transparent;border-top-color:var(--ink)}
.search-btn{position:absolute;left:0;bottom:0;width:216px;height:30px;background:var(--ink);color:var(--white);font-weight:700;font-size:15px;text-align:center;line-height:30px;letter-spacing:1px}
.nav-search{position:absolute;left:862px;width:216px;height:34px;background:#555}

/* what we do */
.what{position:absolute;left:0;top:670px;width:1200px;height:440px;background:var(--white)}
.what .section-title{margin-top:34px}
.service{position:absolute;top:115px;width:300px;text-align:center}
.icon-ring{width:136px;height:136px;border:3px solid #ccc;border-radius:50%;margin:0 auto;display:flex;align-items:center;justify-content:center}
.icon-core{width:112px;height:112px;border-radius:50%;border:2px solid var(--ink);display:flex;align-items:center;justify-content:center}
.icon-core.filled{background:var(--ink)}
.service h3{font-size:23px;line-height:30px;font-weight:700;color:var(--ink);margin:12px 0 6px}
.service p{font-size:12px;line-height:1.3;color:#333}
.more-dot{width:28px;height:28px;border-radius:50%;border:1px solid #ccc;margin:8px auto 0;display:flex;align-items:center;justify-content:center}
.more-dot.dark{background:var(--ink);border-color:var(--ink)}

/* how to */
.howto{position:absolute;left:0;top:1110px;width:1200px;height:462px}
.howto-bg{position:absolute;inset:0;background:linear-gradient(180deg,#ededed 0%,#e2e3e2 45%,#c9ccc6 75%,#b7b9b0 100%)}
.howto .section-title{position:absolute;top:30px;width:100%}
.step{position:absolute;top:111px;width:318px;height:260px;background:rgba(255,255,255,.92);text-align:center}
.step.current{background:rgba(35,31,32,.88);color:var(--white)}
.step-num{width:58px;height:58px;border:3px solid var(--ink);border-radius:50%;margin:18px auto 0;font-size:26px;line-height:52px;font-family:"Questrial",sans-serif}
.step.current .step-num{border-color:var(--white)}
.step h3{font-size:24px;font-weight:700;margin:18px 0 8px;color:var(--ink)}
.step.current h3{color:var(--green)}
.step p{font-size:12px;line-height:1.35;padding:0 22px}
.step .read{position:absolute;left:0;bottom:0;width:100%;height:36px;background:var(--ink);color:var(--green);font-size:15px;line-height:36px}

/* venue */
.venue{position:absolute;left:0;top:1572px;width:1200px;height:438px;background:var(--ink);color:var(--white)}
.venue .section-title{color:#ddd;margin-top:26px}
.venue-photo{position:absolute;left:101px;top:108px;width:430px;height:285px;background:linear-gradient(135deg,#d9a06a 0%,#8a5a3c 35%,#5d7fa3 65%,#9db6cc 100%)}
.venue-copy{position:absolute;left:545px;top:110px;width:625px}
.venue-copy h3{color:var(--green);font-size:22px;font-weight:700;margin-bottom:10px}
.venue-copy p{font-size:15px;line-height:1.4;margin-bottom:16px;text-align:justify}
.btn-list{position:absolute;left:545px;top:355px;width:214px;height:44px;background:var(--green);color:var(--ink);font-weight:700;font-size:18px;text-align:center;line-height:44px}

/* newsletter */
.newsletter{position:absolute;left:0;top:2010px;width:1200px;height:106px;background:var(--green)}
.newsletter span{position:absolute;left:205px;top:37px;color:var(--white);font-family:"Questrial",sans-serif;font-size:24px}
.newsletter .email{position:absolute;left:570px;top:37px;width:320px;height:34px;background:var(--white);font-size:12px;color:var(--muted);padding:9px 10px}
.newsletter .submit{position:absolute;left:890px;top:37px;width:108px;height:34px;background:var(--ink);color:var(--white);font-weight:700;font-size:15px;text-align:center;line-height:34px}

/* contact */
.contact{position:absolute;left:0;top:2116px;width:1200px;height:295px}
.contact-map{position:absolute;inset:0;background:linear-gradient(90deg,#e8e1cf 0%,#efeadc 55%,#dfe6e9 75%,#a9c4d6 100%)}
.contact-card{position:absolute;left:313px;top:61px;width:577px;height:186px;background:rgba(255,255,255,.92);text-align:center}
.contact-card h2{font-family:"Questrial",sans-serif;font-weight:400;font-size:40px;margin-top:14px;color:#333}
.contact-card p{font-size:15px;margin-top:6px}
.contact-card .lines{font-size:24px;margin-top:8px;color:var(--ink)}

/* footer */
.site-footer{position:absolute;left:0;top:2411px;width:1200px;height:204px;background:var(--ink);color:var(--white)}
.site-footer h4{font-size:18px;font-weight:700;position:absolute;top:14px}
.site-footer ul{list-style:none;position:absolute;top:48px;font-size:12px;line-height:20px}
.site-footer ul li::before{content:"• "}
.social li::before{content:none!important}
.social li{display:flex;align-items:center;gap:8px;line-height:27px}
.social .dot{width:20px;height:20px;border-radius:50%;background:var(--white)}
.support{position:absolute;left:579px;top:48px;width:200px;font-size:12px;line-height:20px}
.foot-brand{position:absolute;left:930px;top:20px;width:160px;text-align:center}
.foot-brand .mark{width:72px;height:72px;border:3px solid var(--white);border-radius:50%;margin:0 auto 8px}
.cards{display:flex;gap:5px;justify-content:center;margin-top:10px}
.cards span{width:26px;height:17px;background:var(--white);border-radius:2px}
.copyright{position:absolute;left:0;top:2615px;width:1200px;height:40px;background:var(--white);text-align:center;font-size:12px;line-height:40px;color:#333}
</style>
</head>
<body>

<header class="hero">
  <div class="hero-photo" role="img" aria-label="Aerial photo of a harbour city skyline with tower and water"></div>
  <div class="brand-box">
    <div class="mark"></div>
    <div class="brand-name">galbrook</div>
  </div>

  <form class="search-panel">
    <div class="head">
      <svg width="14" height="18" viewBox="0 0 14 18"><path d="M7 0a7 7 0 0 0-7 7c0 5 7 11 7 11s7-6 7-11a7 7 0 0 0-7-7z" fill="#fff"/><circle cx="7" cy="7" r="2.6" fill="#231f20"/></svg>
      Search galbrook
    </div>
    <label>PROPERTY TYPE</label>
    <div class="field select">SELECT CATEGORY</div>
    <label>LOCATION</label>
    <div class="field select">ALL REGIONS</div>
    <div class="field select">ALL DISTRICTS</div>
    <div class="field select">ALL SUBURBS</div>
    <label>KEYWORDS</label>
    <div class="field">TYPE YOUR KEYWORDS</div>
    <div class="search-btn">SEARCH</div>
  </form>

  <nav class="main-nav">
    <a class="active" style="left:138px">What We Do</a>
    <a style="left:268px">How to Use Our Site</a>
    <a style="left:451px">Are You a Venue ?</a>
    <a style="left:640px">Contact Us</a>
    <div class="burger"><span></span><span></span><span></span></div>
    <div class="nav-search" style="top:10px"></div>
    <svg class="abs" style="left:1045px;top:18px" width="18" height="18" viewBox="0 0 18 18"><circle cx="7" cy="7" r="5.5" stroke="#ccc" stroke-width="2" fill="none"/><path d="M11 11l6 6" stroke="#ccc" stroke-width="2"/></svg>
  </nav>
</header>

<section class="what">
  <h2 class="section-title">What we do...</h2>
  <div class="service" style="left:118px">
    <div class="icon-ring"><div class="icon-core">
      <svg width="70" height="50" viewBox="0 0 70 50"><rect x="12" y="4" width="14" height="18" fill="#231f20"/><rect x="44" y="4" width="14" height="18" fill="#231f20"/><rect x="26" y="14" width="18" height="8" fill="#231f20"/><circle cx="17" cy="32" r="15" fill="#231f20"/><circle cx="53" cy="32" r="15" fill="#231f20"/><circle cx="17" cy="32" r="8" fill="#fff"/><circle cx="53" cy="32" r="8" fill="#fff"/></svg>
    </div></div>
    <h3>We Find</h3>
    <p>Lorem ipsum dolor sit amet, consectetuer adipiscing elit, sed diam nonummy nibh euismod tincidunt ut laoreet dolore magna aliquam erat volutpat. Ut wisi enim ad minim veniam, quis nostrud exerci tation ullamcorper suscipit.</p>
    <div class="more-dot"><svg width="12" height="12" viewBox="0 0 12 12"><path d="M1 6h9M6 2l4 4-4 4" stroke="#bbb" stroke-width="1.6" fill="none"/></svg></div>
  </div>
  <div class="service" style="left:455px">
    <div class="icon-ring"><div class="icon-core filled">
      <svg width="70" height="62" viewBox="0 0 70 62"><path d="M35 2L2 30h8v30h50V30h8z" fill="#fff"/><circle cx="35" cy="30" r="8" fill="#231f20"/><path d="M20 60c0-12 7-18 15-18s15 6 15 18z" fill="#231f20"/></svg>
    </div></div>
    <h3>We Care</h3>
    <p>Lorem ipsum dolor sit amet, consectetuer adipiscing elit, sed diam nonummy nibh euismod tincidunt ut laoreet dolore magna aliquam erat volutpat. Ut wisi enim ad minim veniam, quis nostrud exerci tation ullamcorper suscipit.</p>
    <div class="more-dot dark"><svg width="12" height="12" viewBox="0 0 12 12"><path d="M1 6h9M6 2l4 4-4 4" stroke="#fff" stroke-width="1.8" fill="none"/></svg></div>
  </div>
  <div class="service" style="left:785px">
    <div class="icon-ring"><div class="icon-core">
      <svg width="64" height="56" viewBox="0 0 64 56"><path d="M32 2L2 28h8v26h16V38h12v16h16V28h8z" fill="#231f20"/><rect x="44" y="6" width="7" height="14" fill="#231f20"/></svg>
    </div></div>
    <h3>We Serve</h3>
    <p>Lorem ipsum dolor sit amet, consectetuer adipiscing elit, sed diam nonummy nibh euismod tincidunt ut laoreet dolore magna aliquam erat volutpat. Ut wisi enim ad minim veniam, quis nostrud exerci tation ullamcorper suscipit.</p>
    <div class="more-dot"><svg width="12" height="12" viewBox="0 0 12 12"><path d="M1 6h9M6 2l4 4-4 4" stroke="#bbb" stroke-width="1.6" fill="none"/></svg></div>
  </div>
</section>

<section class="howto">
  <div class="howto-bg" role="img" aria-label="Faded photo of a hillside suburb"></div>
  <h2 class="section-title">How to use our site</h2>
  <div class="step current" style="left:111px">
    <div class="step-num">1</div>
    <h3>Lorem Ipsum</h3>
    <p>Lorem ipsum dolor sit amet, consectetuer adipiscing elit, sed diam nonummy nibh euismod tincidunt ut laoreet dolore magna aliquam erat volutpat. Ut wisi enim ad minim veniam, quis nostrud exerci tation ullamcorper suscipit.</p>
    <div class="read">Read More</div>
  </div>
  <div class="step" style="left:441px">
    <div class="step-num">2</div>
    <h3>Dolor sit amet</h3>
    <p>Lorem ipsum dolor sit amet, consectetuer adipiscing elit, sed diam nonummy nibh euismod tincidunt ut laoreet dolore magna aliquam erat volutpat. Ut wisi enim ad minim veniam, quis nostrud exerci tation ullamcorper suscipit.</p>
    <div class="read">Read More</div>
  </div>
  <div class="step" style="left:775px">
    <div class="step-num">3</div>
    <h3>Sed diam nonummy</h3>
    <p>Lorem ipsum dolor sit amet, consectetuer adipiscing elit, sed diam nonummy nibh euismod tincidunt ut laoreet dolore magna aliquam erat volutpat. Ut wisi enim ad minim veniam, quis nostrud exerci tation ullamcorper suscipit.</p>
    <div class="read">Read More</div>
  </div>
</section>

<section class="venue">
  <h2 class="section-title">Are you a venue ?</h2>
  <div class="venue-photo" role="img" aria-label="Photo of a house deck with glass doors overlooking the sea at sunset"></div>
  <div class="venue-copy">
    <h3>Velit Esse Molestie Consequat</h3>
    <p>Lorem ipsum dolor sit amet, consectetuer adipiscing elit, sed diam nonummy nibh euismod tincidunt ut laoreet dolore magna aliquam erat volutpat. Ut wisi enim ad minim veniam, quis nostrud exerci tation ullamcorper suscipit lobortis nisl ut aliquip ex ea commodo consequat. Duis autem vel eum iriure dolor in hendrerit in vulputate velit esse molestie consequat.</p>
    <p>, vel illum dolore eu feugiat nulla facilisis at vero eros et accumsan et iusto odio dignissim qui blandit praesent luptatum zzril delenit augue duis dolore te feugait nulla facilisi.</p>
  </div>
  <div class="btn-list">HOW TO LIST</div>
</section>

<section class="newsletter">
  <span>Subscribe Our News Letter Here</span>
  <div class="email">ENTER YOUR EMAIL ID HERE</div>
  <div class="submit">SUBMIT</div>
</section>

<section class="contact">
  <div class="contact-map" role="img" aria-label="Street map of the city waterfront"></div>
  <div class="contact-card">
    <h2>Contact us</h2>
    <p>Lorem ipsum dolor sit amet, consectetuer adipiscing elit.</p>
    <div class="lines">+64-555-0142 &nbsp;|&nbsp; info@galbrook.co.nz</div>
  </div>
</section>

<footer class="site-footer">
  <h4 style="left:111px">Quick link</h4>
  <ul style="left:118px">
    <li>What we do</li><li>How to use our site</li><li>Are you a venue ?</li><li>How to list</li><li>About listing</li><li>Contact us</li>
  </ul>
  <ul style="left:248px">
    <li>FAQs</li><li>Listing Fees</li><li>Why venue ?</li><li>Testimonials</li><li>Terms &amp; Conditions</li><li>Privacy Policy</li>
  </ul>
  <h4 style="left:411px">Follow us on</h4>
  <ul class="social" style="left:411px;top:44px">
    <li><span class="dot"></span>Friendwall</li>
    <li><span class="dot"></span>Chirpline</li>
    <li><span class="dot"></span>Circlenet</li>
    <li><span class="dot"></span>Clipstream</li>
  </ul>
  <h4 style="left:579px">For Support</h4>
  <p class="support">Our customer support team is here to help! We are available by phone at +64-555-0142 from 9:30am to 9pm Pacific and by email at support@galbrook.co.nz</p>
  <div class="foot-brand">
    <div class="mark"></div>
    <div class="brand-name" style="font-size:26px">galbrook</div>
    <div class="cards"><span></span><span></span><span></span><span></span><span></span></div>
  </div>
</footer>
<div class="copyright">galbrook.co.nz ©2016. All Right Reserved</div>

</body>
</html>
```